Old Fashioned, Artisan Goat Milk Soap Label

We are branching out in our goat milk dairy into artisan goat milk soaps. High quality, yet an old fashioned feel. Simple yet elegant. Emphasis on the milk and its moisturizing, healing, softening, and superiority.
Purity in a simple design that harkens back to a quaint, earlier time where quality ingredients were valued as much as quality workmanship.
Perhaps a drop symbolizing the milk, or a bucket pouring into or out of the logo. We already have our farm logo, Willowbrook Hollow, and were thinking the soap would be "Sweet Nell"
The labels will grace our liquid soap bottles and our bar soaps. 3.5" X 2.5"
The label color will be an antiqued ivory or other shade to convey a simpler time.

Reason: Realized that the contest length was short enough to scare away designers. Adding time to give entered designers time to create.

Target Market(s)

Upscale people looking to know where their products come from. People looking for better options, artisan products.

Requirements
Must have
• My project must have emphasis on the milk, old time feel, simple elegance
Nice to have
• Perhaps a drop symbolizing the milk, or a bucket pouring into or out of the logo. We already have our farm logo, Willowbrook Hollow, and were thinking the soap would be "Sweet Nell"
• If you use a goat, please be aware that we have the breed Nubians that have long luxurious ears and don't have horns.

```html
<!DOCTYPE html>
<html lang="en">
<head>
<meta charset="utf-8">
<title>Willowbrook Hollow – Sweet Nell Goats Milk Soap Label</title>
<link href="https://fonts.googleapis.com/css2?family=Cinzel:wght@400;700&family=Libre+Caslon+Text&display=swap" rel="stylesheet">
<style>
  :root {
    --ivory: #f3eec9;
    --ivory-shade: #e9e2b8;
    --navy: #1e2048;
    --sage: #8fae5f;
    --sage-soft: #b9cd93;
    --cream-line: #efe9cf;
  }
  * { box-sizing: border-box; margin: 0; padding: 0; }
  html, body {
    width: 1200px;
    height: 898px;
    overflow: hidden;
    background: var(--ivory);
  }
  .label {
    position: relative;
    width: 1200px;
    height: 898px;
    background: linear-gradient(180deg, var(--ivory) 0%, var(--ivory-shade) 100%);
    color: var(--navy);
    font-family: "Cinzel", serif;
  }
  .corner-ornament {
    position: absolute;
    width: 110px;
    height: 78px;
    border-radius: 40px;
    background: radial-gradient(ellipse at center, var(--sage-soft) 0%, rgba(185,205,147,0) 72%);
  }
  .corner-ornament.top-left { left: 24px; top: 120px; }
  .corner-ornament.top-right { right: 24px; top: 120px; }
  .corner-ornament.bottom-left { left: 24px; top: 770px; }
  .corner-ornament.bottom-right { right: 24px; top: 770px; }

  .farm-name {
    position: absolute;
    top: 250px;
    left: 0;
    width: 100%;
    text-align: center;
    font-size: 62px;
    font-weight: 700;
    letter-spacing: 2px;
    color: var(--navy);
  }
  .farm-location {
    position: absolute;
    top: 342px;
    left: 0;
    width: 100%;
    text-align: center;
    font-family: "Libre Caslon Text", serif;
    font-size: 15px;
    letter-spacing: 1.5px;
    color: var(--navy);
  }
  .milk-drop {
    position: absolute;
    left: 572px;
    top: 432px;
    width: 56px;
    height: 76px;
  }
  .flourish {
    position: absolute;
    left: 420px;
    width: 360px;
    height: 34px;
    border-radius: 17px;
    background: radial-gradient(ellipse at center, var(--sage) 0%, rgba(143,174,95,0.35) 45%, rgba(143,174,95,0) 75%);
  }
  .flourish.above-band { top: 520px; }
  .flourish.below-band { top: 662px; }

  .name-band {
    position: absolute;
    top: 568px;
    left: 0;
    width: 100%;
    height: 84px;
    background: var(--navy);
    display: flex;
    align-items: center;
    justify-content: center;
  }
  .band-rule {
    flex: 1;
    height: 9px;
    border-top: 2px solid var(--cream-line);
    border-bottom: 2px solid var(--cream-line);
  }
  .band-rule.left { margin-left: 0; }
  .band-rule.right { margin-right: 0; }
  .product-name {
    padding: 0 44px;
    font-size: 58px;
    font-weight: 400;
    letter-spacing: 2px;
    color: var(--cream-line);
    white-space: nowrap;
  }
  .product-type {
    position: absolute;
    top: 742px;
    left: 0;
    width: 100%;
    text-align: center;
    font-size: 42px;
    font-weight: 400;
    letter-spacing: 1px;
    color: var(--navy);
  }
  .product-rule {
    position: absolute;
    top: 806px;
    left: 332px;
    width: 536px;
    border-top: 2px solid var(--navy);
  }
  .product-note {
    position: absolute;
    top: 818px;
    left: 0;
    width: 100%;
    text-align: center;
    font-family: "Libre Caslon Text", serif;
    font-size: 29px;
    color: var(--navy);
  }
</style>
</head>
<body>
  <main class="label">
    <div class="corner-ornament top-left" role="img" aria-label="Green leafy corner flourish"></div>
    <div class="corner-ornament top-right" role="img" aria-label="Green leafy corner flourish"></div>
    <div class="corner-ornament bottom-left" role="img" aria-label="Green leafy corner flourish"></div>
    <div class="corner-ornament bottom-right" role="img" aria-label="Green leafy corner flourish"></div>

    <h1 class="farm-name">Willowbrook Hollow</h1>
    <p class="farm-location">MILLBROOK, TX</p>

    <svg class="milk-drop" viewBox="0 0 56 76" aria-label="Milk drop">
      <path d="M28 2 C36 20 52 36 52 50 A24 24 0 0 1 4 50 C4 36 20 20 28 2 Z" fill="var(--navy)"/>
      <path d="M14 50 A14 14 0 0 0 36 62" fill="none" stroke="var(--cream-line)" stroke-width="5" stroke-linecap="round"/>
    </svg>

    <div class="flourish above-band" role="img" aria-label="Green leaf scroll ornament"></div>

    <div class="name-band">
      <span class="band-rule left"></span>
      <h2 class="product-name">SWEET NELL</h2>
      <span class="band-rule right"></span>
    </div>

    <div class="flourish below-band" role="img" aria-label="Green leaf scroll ornament"></div>

    <p class="product-type">GOATS MILK SOAP</p>
    <div class="product-rule"></div>
    <p class="product-note">No extra additives, colors, or fragrances</p>
  </main>
</body>
</html>
```